Etiketten-Design für Honiggläser
Die Zusammenarbeit mit Jorin war sehr unkompliziert. Änderungswünsche wurden prompt umgesetzt und die Beratung war hervorragend! Besten Dank für das tolle Etikett!
Zielgruppe
Wir sind Imker und benötigen Etiketten für Honiggläser.
Aufgabenstellung
Siehe Anlage. Es sollen keine Fotos verwendet werden. Grafiken sind in Ordnung.
Etiketten-Design für Honigglas Etiketten-Design für Honigglas"
Format: Etikett für 250-gr.-Honigglas (TO ∅ 63 mm). Standardmaßgrösse 165 × 40 mm Design: schlicht, hochwertig, modern, edel/royal, unkonventionelles Design (weg von Bienen, Waben, Landschaften usw.), dunkle Farbtöne in Kontrast zu heller Schrift, die beiden Textbausteine 'Los Nr. ' sowi..
Attraktives Etiketten-Design für Honig Attraktives Etiketten-Design für Honig"
Wir verkaufen zur Zeit vor allem Waldhonig, streben aber auch einen Blütenhonig an. Das Etikett soll daher entweder den Wald wiederspiegeln oder aber neutral sein, so dass der Schriftzug Waldhonig oder Blütenhonig jeweils eingesetzt werden kann. Wichtig ist mir der Ortszusatz 'aus dem Glottertal..
Etiketten-Design für Produkte eines Familienbetriebs mit Imkerei und Hühnerhaltung Etiketten-Design für Produkte eines Familienbetriebs mit Imkerei und Hühnerhaltung"
1. Zentrale, auf allen Etiketten wiederkehrende Elemente: - Unser Riegelhaus (stilisiert) (Bild beiliegend) - Das Wort 'Weidlek' (Anmerkung: ohne Anführungszeichen) - die zentralen Elemente sollen die Produkte nicht überragen. 2. Dezente Adresse: - Familie Rattinger, Mühlgrund, CH-9617 Brüsel 3...
Etiketten-Design für Kurkuma-Honig Etiketten-Design für Kurkuma-Honig"
Etikett für 500g // Stanze eckig (210x35mm), Druckdatei entsprechend Vorgaben https://klebwerkstatt.de/faq/ Vorgaben für das Grünfeld Logo im Anhang Vorgaben für EG Öko Logo : https://oekosiegel-muster.eu/landbau/organic/downloads/logo_de Pflichtangaben auf dem Etikett: Gewicht, Adresse siehe Beispiel..
Etiketten-Design für Blütenhonig und Waldhonig gesucht Etiketten-Design für Blütenhonig und Waldhonig gesucht"
Zwei verschiedene Etiketten-Desings 1 x Blütenhonig sowie 1 x Waldhonig für unterschiedliche Honigglasgrößen (500 g und 250 g) Die Maße für die Etiketten wären: Für 500-Gramm-Glas 210 mm x 45 mm für's 250-Gramm-Glas 180 mm x 38 mm. Wir sind auch offen für neue Vorschläge bezüglich ..

```html
<!DOCTYPE html>
<html lang="de">
<head>
<meta charset="utf-8">
<title>Etikett Bayerischer Bienenhonig Sommertracht</title>
<link href="https://fonts.googleapis.com/css2?family=Jost:wght@300;400;500;600&family=Montserrat:wght@400;700&display=swap" rel="stylesheet">
<style>
  :root {
    --bg: #e6e5e3;
    --strip-orange: #f4ae2f;
    --label-teal: #aed2ce;
    --ink: #231f20;
    --white: #ffffff;
  }
  * { margin: 0; padding: 0; box-sizing: border-box; }
  html, body { width: 880px; height: 1200px; overflow: hidden; background: var(--bg); }
  .canvas { position: relative; width: 880px; height: 1200px; }

  .lid-strip {
    position: absolute; left: 336px; top: 177px;
    width: 175px; height: 525px;
    background: var(--strip-orange);
    overflow: hidden;
  }
  .brand {
    display: flex; align-items: center; gap: 8px;
    font-family: "Jost", sans-serif; font-weight: 500;
    font-size: 15px; line-height: 1.05; color: var(--ink);
    text-transform: uppercase; letter-spacing: 0.03em;
    white-space: nowrap;
  }
  .strip-brand { position: absolute; left: 22px; top: 52px; }
  .brand-square { width: 28px; height: 28px; background: var(--ink); flex: none; }

  .body-label {
    position: absolute; left: 60px; top: 702px;
    width: 760px; height: 321px;
    background: var(--label-teal);
  }
  .date-field {
    position: absolute; right: 0; top: 0;
    width: 57px; height: 100%;
    background: var(--white);
  }

  .side-text {
    position: absolute; bottom: 16px;
    writing-mode: vertical-rl; transform: rotate(180deg);
    font-family: "Montserrat", sans-serif; font-weight: 400;
    font-size: 12.5px; line-height: 14.5px; color: var(--ink);
    text-align: left;
  }
  .side-text b { font-weight: 700; }
  .side-text.usage { left: 14px; height: 285px; }
  .side-text.producer { left: 618px; height: 300px; }
  .side-text.best-before { left: 715px; height: 150px; }

  .front {
    position: absolute; left: 321px; top: 40px;
    font-family: "Jost", sans-serif; color: var(--ink);
  }
  .front-brand { margin-left: -30px; margin-bottom: 22px; }
  .product-line {
    font-weight: 500; font-size: 20px; line-height: 19px;
    letter-spacing: 0.03em; text-transform: uppercase;
  }
  .variety {
    font-weight: 300; font-size: 25px; line-height: 26px;
    letter-spacing: 0.06em; color: var(--white);
    text-transform: uppercase; margin-top: 1px;
  }
  .composition {
    font-weight: 400; font-size: 13.5px; line-height: 17px;
    letter-spacing: 0.03em; text-transform: uppercase; margin-top: 10px;
  }
  .weight {
    font-family: "Montserrat", sans-serif; font-weight: 700;
    font-size: 23px; margin-top: 28px; letter-spacing: 0.02em;
  }
</style>
</head>
<body>
<div class="canvas">
  <div class="lid-strip">
    <div class="brand strip-brand"><span class="brand-square"></span><span>Imkerei<br>Brandauer</span></div>
  </div>

  <div class="body-label">
    <p class="side-text usage"><b>Hinweis:</b> Bienenhonig kristallisiert bei<br>längerer Lagerung. Durch Erwärmen im<br>Wasserbad bei 40° C kann Honig<br>ohne Schaden wieder verflüssigt werden.<br><b>Mehrwegglas</b> - Bitte zurück zum Imker</p>

    <div class="front">
      <div class="brand front-brand"><span class="brand-square"></span><span>Imkerei<br>Brandauer</span></div>
      <p class="product-line">Bayerischer<br>Bienenhonig</p>
      <p class="variety">Sommertracht</p>
      <p class="composition">Blütenhonig &amp;<br>Honigtau</p>
      <p class="weight">500 g</p>
    </div>

    <p class="side-text producer"><b>Imkerei Brandauer,</b> Wiesengrund 14,<br>85399 Tannhausen.<br>Email:info@imkerei-brandauer.de<br>Lagerhinweis: Kühl, dunkel und trocken lagern.<br>Ursprungsland: Bayern, Deutschland.</p>

    <div class="date-field"></div>
    <p class="side-text best-before">Mindestens haltbar bis:</p>
  </div>
</div>
</body>
</html>
```